Stationary/business card/envelope design for Larkvale Dentalcare

We are located in the foothills of the sierra nevada mountains. We are looking for a beautiful classy modern stationary. We need evelopes and business card design all to flow seamlessly. Envelope design.

Additional office address 4816 Meridian Wy., Suite B, Auburn, CA 95604 Phone: pending Fax: pending.

3 different Drs on each business card:
Helen R. Marsh, DDS
Orla P. Marsh, DDS
Rebecca S. Halvey, DDS

Target Market(s)

Dental patients

Industry/Entity Type

Dental

Contact Information for Business Card

Two sided. See example.

Font styles to use
Sans Serif

Requirements
Must have
• One sided business cards. Need envelope design.
Colors should match existing logo.

Helen R. Marsh, DDS
Orla P. Marsh, DDS
Rebecca S. Halvey, DDS

```html
<!DOCTYPE html>
<html lang="en">
<head>
<meta charset="utf-8">
<title>Larkvale Dentalcare – Stationery</title>
<link rel="stylesheet" href="https://fonts.googleapis.com/css2?family=Arimo:wght@400;700&display=swap">
<style>
  :root {
    --stage: #f7f7f7;
    --paper: #f9f9f9;
    --card: #ffffff;
    --ink: #222222;
    --label: #2b2b2b;
    --muted: #8a8a8a;
    --blue: #45b0d6;
    --green-1: #7aab3a;
    --green-2: #5a9a45;
    --green-3: #2f8a4a;
    --brand-green: #2e7d4f;
    --shadow: 0 0 14px rgba(0,0,0,.32);
  }
  * { box-sizing: border-box; margin: 0; padding: 0; }
  html, body { width: 1080px; height: 1200px; overflow: hidden; background: #fff; }
  body { font-family: "Arimo", Arial, sans-serif; color: var(--ink); position: relative; }

  .stage { position: absolute; left: 0; top: 0; width: 1080px; height: 983px; background: var(--stage); }

  .section-title { position: absolute; font-size: 19px; color: var(--label); transform: translateX(-50%); white-space: nowrap; }
  .side-label { position: absolute; font-size: 10px; color: var(--muted); transform: translateX(-50%); }

  .sheet { position: absolute; background: var(--paper); box-shadow: var(--shadow); overflow: hidden; }

  .brand-bar { position: absolute; left: 0; right: 0; bottom: 0; }
  .brand-bar span { position: absolute; top: 0; bottom: 0; }
  .brand-bar .sq1 { background: var(--green-1); }
  .brand-bar .sq2 { background: var(--green-2); }
  .brand-bar .sq3 { background: var(--green-3); }
  .brand-bar .band { background: var(--blue); right: 0; }

  .brand { position: absolute; display: flex; align-items: center; gap: 6px; color: var(--brand-green); font-weight: 700; line-height: 1.1; }
  .brand .dot { flex: none; border-radius: 50%; background: var(--blue); }

  .contact-list { position: absolute; list-style: none; }
  .contact-list li { display: flex; align-items: flex-start; white-space: nowrap; }
  .contact-list svg { flex: none; fill: var(--blue); }

  /* Letterhead */
  .letterhead { left: 33px; top: 181px; width: 450px; height: 637px; }
  .letterhead .brand { left: 28px; top: 42px; font-size: 13px; }
  .letterhead .brand .dot { width: 34px; height: 34px; }
  .letterhead .contact-list { left: 295px; top: 28px; font-size: 8px; line-height: 11.5px; }
  .letterhead .contact-list li svg { width: 9px; height: 9px; margin: 1px 6px 0 0; }
  .letterhead .brand-bar { height: 9px; }

  /* Envelope */
  .envelope-front { left: 554px; top: 76px; width: 505px; height: 243px; }
  .envelope-front .brand { left: 22px; top: 40px; font-size: 11px; }
  .envelope-front .brand .dot { width: 28px; height: 28px; }
  .envelope-front .return-line { position: absolute; bottom: 20px; font-size: 7px; display: flex; align-items: center; gap: 4px; }
  .envelope-front .return-line svg { width: 8px; height: 8px; fill: var(--blue); }
  .envelope-front .address { left: 24px; }
  .envelope-front .web { right: 30px; }
  .envelope-front .brand-bar { height: 10px; }

  .envelope-back { left: 554px; top: 382px; width: 505px; height: 244px; }
  .envelope-back .flap { position: absolute; left: 0; top: 0; width: 505px; height: 95px; }

  /* Business cards */
  .card { top: 719px; width: 224px; height: 127px; background: var(--card); border-radius: 7px; box-shadow: 0 0 8px rgba(0,0,0,.3); border: 1px solid #555; }
  .card .brand-bar { height: 8px; }
  .card-back { left: 558px; }
  .card-back .brand { left: 50%; top: 48px; transform: translateX(-50%); font-size: 11px; }
  .card-back .brand .dot { width: 28px; height: 28px; }
  .card-front { left: 817px; }
  .card-front .brand { left: 14px; top: 22px; font-size: 9px; }
  .card-front .brand .dot { width: 20px; height: 20px; }
  .card-front .holder { position: absolute; right: 13px; top: 28px; text-align: right; }
  .card-front .holder .name { font-size: 8px; font-weight: 700; color: var(--ink); }
  .card-front .holder .role { font-size: 5.5px; color: var(--ink); margin-top: 1px; }
  .card-front .contact-list { font-size: 5.5px; line-height: 8px; }
  .card-front .contact-list li svg { width: 6px; height: 6px; margin: 1px 4px 0 0; }
  .card-front .location { left: 14px; top: 87px; }
  .card-front .lines { left: 131px; top: 81px; }
</style>
</head>
<body>
<svg width="0" height="0" style="position:absolute">
  <defs>
    <symbol id="i-phone" viewBox="0 0 16 16"><path d="M2 6c0-2 2-3 6-3s6 1 6 3v1h-3V6H5v1H2zM4 8h8l1 5H3z"/></symbol>
    <symbol id="i-fax" viewBox="0 0 16 16"><path d="M4 1h8v4H4zM1 6h14v6h-3v3H4v-3H1zM5 10v4h6v-4z"/></symbol>
    <symbol id="i-mail" viewBox="0 0 16 16"><path d="M1 3h14v10H1zM2.5 4.5 8 9l5.5-4.5z" fill-rule="evenodd"/></symbol>
    <symbol id="i-globe" viewBox="0 0 16 16"><path d="M8 1a7 7 0 1 0 0 14A7 7 0 0 0 8 1zm0 1.5c.8 1 1.4 2.4 1.6 4H6.4C6.6 4.9 7.2 3.5 8 2.5zM2.6 6.5h2.3c.1-1.3.5-2.6 1.1-3.6a5.5 5.5 0 0 0-3.4 3.6zm8.5 0h2.3a5.5 5.5 0 0 0-3.4-3.6c.6 1 1 2.3 1.1 3.6zM2.6 9.5a5.5 5.5 0 0 0 3.4 3.6c-.6-1-1-2.3-1.1-3.6zm3.8 0c.2 1.6.8 3 1.6 4 .8-1 1.4-2.4 1.6-4zm4.7 0c-.1 1.3-.5 2.6-1.1 3.6a5.5 5.5 0 0 0 3.4-3.6zM2.5 8h2.3M11.2 8h2.3"/></symbol>
    <symbol id="i-pin" viewBox="0 0 16 16"><path d="M8 1a5 5 0 0 0-5 5c0 3.5 5 9 5 9s5-5.5 5-9a5 5 0 0 0-5-5zm0 3a2 2 0 1 1 0 4 2 2 0 0 1 0-4z" fill-rule="evenodd"/></symbol>
  </defs>
</svg>

<div class="stage">
  <h2 class="section-title" style="left:248px; top:136px;">Letterhead</h2>
  <h2 class="section-title" style="left:807px; top:26px;">Envelope Front</h2>
  <h2 class="section-title" style="left:807px; top:338px;">Envelope Back</h2>
  <h2 class="section-title" style="left:790px; top:672px;">Business Card</h2>
  <span class="side-label" style="left:670px; top:689px;">Back</span>
  <span class="side-label" style="left:929px; top:689px;">Front</span>

  <section class="sheet letterhead">
    <div class="brand"><span class="dot"></span><span>Larkvale<br>Dentalcare</span></div>
    <ul class="contact-list">
      <li><svg><use href="#i-phone"/></svg>530-555-0142</li>
      <li><svg><use href="#i-fax"/></svg>530-555-0187</li>
      <li><svg><use href="#i-mail"/></svg>hrmarsh@larkvalemail.com</li>
      <li style="margin-top:2px"><svg><use href="#i-globe"/></svg>www.larkvaledentalcare.com</li>
      <li style="margin-top:3px"><svg><use href="#i-pin"/></svg>4816 Meridian Wy., Suite B,<br>Auburn, CA 95604</li>
    </ul>
    <div class="brand-bar">
      <span class="sq1" style="left:0; width:19px"></span>
      <span class="sq2" style="left:29px; width:19px"></span>
      <span class="sq3" style="left:57px; width:19px"></span>
      <span class="band" style="left:86px"></span>
    </div>
  </section>

  <section class="sheet envelope-front">
    <div class="brand"><span class="dot"></span><span>Larkvale<br>Dentalcare</span></div>
    <p class="return-line address"><svg><use href="#i-pin"/></svg>4816 Meridian Wy., Suite B, Auburn, CA 95604</p>
    <p class="return-line web"><svg><use href="#i-globe"/></svg>www.larkvaledentalcare.com</p>
    <div class="brand-bar">
      <span class="sq1" style="left:0; width:22px"></span>
      <span class="sq2" style="left:32px; width:22px"></span>
      <span class="sq3" style="left:64px; width:22px"></span>
      <span class="band" style="left:96px"></span>
    </div>
  </section>

  <section class="sheet envelope-back">
    <svg class="flap" viewBox="0 0 505 95"><polygon points="0,2 505,2 497,85 17,90" fill="var(--blue)"/></svg>
  </section>

  <section class="sheet card card-back">
    <div class="brand"><span class="dot"></span><span>Larkvale<br>Dentalcare</span></div>
    <div class="brand-bar">
      <span class="sq1" style="left:0; width:11px"></span>
      <span class="sq2" style="left:17px; width:11px"></span>
      <span class="sq3" style="left:35px; width:11px"></span>
      <span class="band" style="left:52px"></span>
    </div>
  </section>

  <section class="sheet card card-front">
    <div class="brand"><span class="dot"></span><span>Larkvale<br>Dentalcare</span></div>
    <div class="holder">
      <p class="name">Helen R. Marsh, DDS</p>
      <p class="role">Family &amp; Cosmetic Dentistry</p>
    </div>
    <ul class="contact-list location">
      <li><svg><use href="#i-pin"/></svg>4816 Meridian Wy.,<br>Suite B, Auburn, CA 95604</li>
      <li><svg><use href="#i-globe"/></svg>www.larkvaledentalcare.com</li>
    </ul>
    <ul class="contact-list lines">
      <li><svg><use href="#i-phone"/></svg>530-555-0142</li>
      <li style="margin-top:2px"><svg><use href="#i-fax"/></svg>530-555-0187</li>
      <li style="margin-top:2px"><svg><use href="#i-mail"/></svg>hrmarsh@larkvalemail.com</li>
    </ul>
    <div class="brand-bar">
      <span class="sq1" style="left:0; width:11px"></span>
      <span class="sq2" style="left:17px; width:11px"></span>
      <span class="sq3" style="left:35px; width:11px"></span>
      <span class="band" style="left:52px"></span>
    </div>
  </section>
</div>
</body>
</html>
```